New Meal Prep Flyer for New Package Deals

We are looking for a design that displays our new packages that we offer. If you take a look at our website www.copperspoonpantry.com, and click on packages , you'll see the way we display them currently . We would like something similar to that in style . The first package is called "Evergreen" and this package will be a 1 week package (7 days ), 2 meals a day, for a price of $195.00. The second package is called "Pebble" and this package will be a 3 week package (21 days) 2 meals per day, for a price of $546.00 , the third package is a 6 week+ package (45 days), and it is called "Lighthouse" , 2 meals per day , and the price is $1080.00 .
For the Pebble Package , can you put next to it "Save $42.00!"
For the Lighthouse Package, can you put next to it "Save $180!"
We also want our logo on the flyer (see attached), and we are just looking for a 1 page flyer , 8 1/2 x 11.

```html
<!DOCTYPE html>
<html lang="en">
<head>
<meta charset="utf-8">
<title>Copper Spoon Meal Prep Packages</title>
<link rel="stylesheet" href="https://fonts.googleapis.com/css2?family=DM+Sans:wght@500;700&family=Montserrat:wght@800;900&family=Oswald:wght@600&family=Playball&display=swap">
<style>
  :root {
    --green: #86b33b;
    --green-dark: #6f9a2a;
    --charcoal: #545456;
    --light: #ececec;
    --paper: #efefef;
    --url-tab: #f4f4f4;
    --white: #ffffff;
    --ink: #1d1d1d;
    --logo-gray: #8f8f8f;
  }
  html, body { margin: 0; padding: 0; overflow: hidden; }
  .flyer {
    position: relative; width: 900px; height: 1200px; overflow: hidden;
    background: var(--paper); font-family: "Montserrat", sans-serif;
  }
  .brand { position: absolute; top: 58px; left: 0; width: 900px; text-align: center; }
  .brand-name {
    display: inline-flex; align-items: center; gap: 14px;
    font-family: "Montserrat", sans-serif; font-weight: 900; font-size: 52px;
    letter-spacing: 2px; color: var(--logo-gray); line-height: 1;
  }
  .brand-dot { width: 18px; height: 18px; border-radius: 50%; background: var(--green); }
  .brand-tagline {
    margin-top: 10px; font-family: "DM Sans", sans-serif; font-weight: 700;
    font-size: 19px; color: var(--green); letter-spacing: .2px;
  }
  .headline-band {
    position: absolute; top: 185px; left: 0; width: 900px; height: 140px;
    background: var(--charcoal); text-align: center;
    font-family: "DM Sans", sans-serif; font-weight: 700; font-size: 44px; line-height: 48px;
  }
  .headline-band .line-1 { color: var(--white); padding-top: 20px; }
  .headline-band .line-2 { color: var(--green); }
  .food-photo {
    position: absolute; top: 325px; left: 0; width: 900px; height: 744px;
    background: radial-gradient(circle at 30% 40%, #7fb23a 0%, #5d9431 45%, #4b7d2b 100%);
  }
  .card-shapes { position: absolute; top: 0; left: 0; }
  .site-url {
    position: absolute; top: 386px; left: 300px; width: 440px;
    font-family: "DM Sans", sans-serif; font-weight: 700; font-size: 20px;
    letter-spacing: 5.2px; color: var(--charcoal); white-space: nowrap;
  }
  .tier-label {
    position: absolute; font-family: "Playball", cursive; font-size: 40px;
    color: var(--white); white-space: nowrap; line-height: 1;
  }
  .tier-evergreen { left: 110px; top: 552px; transform: translate(-50%, -50%) rotate(-90deg); }
  .tier-pebble { left: 790px; top: 538px; transform: translate(-50%, -50%) rotate(-90deg); }
  .tier-lighthouse {
    left: 300px; top: 700px; transform: translateX(-50%);
    font-size: 33px; line-height: 36px;
  }
  .package { position: absolute; }
  .package-title { font-weight: 900; font-size: 30px; line-height: 28px; letter-spacing: .5px; }
  .package-days {
    display: inline-block; margin-top: 3px; padding: 0 3px;
    font-weight: 900; font-size: 19px; line-height: 23px;
  }
  .package-meals {
    width: 172px; border-top: 1.5px solid currentColor; border-bottom: 1.5px solid currentColor;
    font-weight: 900; font-size: 16.5px; letter-spacing: 1px; line-height: 32px; white-space: nowrap;
  }
  .package-price-label {
    display: flex; align-items: flex-end; gap: 2px; margin-top: 8px;
    font-weight: 900; font-size: 17px; line-height: 17px;
  }
  .leaf { width: 26px; height: 22px; }
  .package-price {
    font-family: "Oswald", sans-serif; font-weight: 600; font-size: 60px; line-height: 62px;
    letter-spacing: -1px;
  }
  .package-price .currency { font-size: 32px; }
  .package-week-1 { left: 178px; top: 444px; color: var(--white); }
  .package-week-1 .package-days { background: var(--charcoal); color: var(--white); }
  .package-week-1 .package-meals { margin-top: 10px; }
  .package-week-3 { left: 479px; top: 444px; color: var(--white); }
  .package-week-3 .package-days { background: var(--white); color: var(--charcoal); }
  .package-week-3 .package-meals { margin-top: 10px; }
  .package-week-3 .package-price-label,
  .package-week-3 .package-price { color: var(--green); }
  .package-week-6 { left: 178px; top: 772px; color: var(--green); }
  .package-week-6 .package-days { background: var(--charcoal); color: var(--white); }
  .package-week-6-detail { position: absolute; left: 470px; top: 745px; color: var(--charcoal); }
  .package-week-6-detail .package-meals { width: 172px; }
  .package-week-6-detail .package-price-label,
  .package-week-6-detail .package-price { color: var(--green); }
  .save-badge {
    position: absolute; width: 84px; height: 84px; border-radius: 50%;
    background: var(--green); color: var(--white); text-align: center;
    box-shadow: 0 0 0 4px var(--green); outline: 3px dotted var(--green); outline-offset: 3px;
    display: flex; flex-direction: column; justify-content: center; font-weight: 900;
  }
  .save-badge .save-word { font-size: 16px; line-height: 17px; }
  .save-badge .save-amount { font-size: 25px; line-height: 26px; }
  .save-badge .currency { font-size: 17px; }
  .badge-42 { left: 662px; top: 443px; }
  .badge-180 { left: 362px; top: 763px; }
  .app-strip { position: absolute; top: 1094px; left: 0; width: 900px; height: 46px; }
  .app-strip-label {
    position: absolute; left: 151px; top: 10px; font-family: "DM Sans", sans-serif;
    font-weight: 700; font-size: 19px; color: var(--ink);
  }
  .store-badge { position: absolute; top: 0; height: 45px; border-radius: 6px; background: var(--ink); }
  .store-badge-a { left: 456px; width: 129px; }
  .store-badge-b { left: 596px; width: 154px; }
  .app-note {
    position: absolute; top: 1144px; left: 0; width: 900px; margin: 0; text-align: center;
    font-family: "DM Sans", sans-serif; font-weight: 500; font-size: 12.5px; color: var(--ink);
  }
  .footer-strip { position: absolute; top: 1182px; left: 0; width: 900px; height: 18px; background: #8d8d8d; }
  .footer-strip svg { display: block; }
</style>
</head>
<body>
<div class="flyer">
  <header class="brand">
    <div class="brand-name"><span class="brand-dot"></span>COPPER SPOON</div>
    <div class="brand-tagline">HEALTHY KITCHEN &nbsp;|&nbsp; MEAL PREP</div>
  </header>

  <section class="headline-band">
    <div class="line-1">Lip-smacking food</div>
    <div class="line-2">at pocket-friendly price!</div>
  </section>

  <div class="food-photo" role="img" aria-label="Overhead photo of fresh meal prep containers with salads, peppers, tomatoes, broccoli and pasta, tinted green"></div>

  <svg class="card-shapes" width="900" height="1200" viewBox="0 0 900 1200" aria-hidden="true">
    <path d="M431 400 H807 V708 H431 Z" fill="var(--charcoal)"/>
    <path d="M113 382 H431 V684 Q431 704 411 704 H93 V402 Q93 382 113 382 Z" fill="var(--green)"/>
    <path d="M226 382 H807 V414 H292 C262 414 252 382 226 382 Z" fill="var(--url-tab)"/>
    <path d="M93 440 L122 455 Q128 458 128 465 V640 Q128 647 122 650 L93 665 Z" fill="var(--charcoal)"/>
    <path d="M807 420 L780 436 Q773 440 773 448 V640 Q773 648 780 650 L807 662 Z" fill="var(--green)"/>
    <path d="M95 708 H805 V875 Q805 895 785 895 H210 Q160 895 140 930 L98 1004 Z" fill="var(--light)" stroke="var(--green)" stroke-width="3"/>
    <path d="M175 704 H422 L414 732 Q412 740 404 740 H205 Q198 740 194 734 Z" fill="var(--charcoal)"/>
  </svg>

  <div class="site-url">www.copperspoonpantry.com</div>

  <div class="tier-label tier-evergreen">Evergreen</div>
  <div class="tier-label tier-pebble">Pebble</div>
  <div class="tier-label tier-lighthouse">Lighthouse</div>

  <div class="package package-week-1">
    <div class="package-title">1 WEEK<br>PACKAGE</div>
    <div class="package-days">(7 DAYS)</div>
    <div class="package-meals">2 MEALS A DAY</div>
    <div class="package-price-label">
      <svg class="leaf" viewBox="0 0 26 22"><path d="M2 21 C2 9 10 2 25 1 C23 14 15 20 5 20 Z" fill="currentColor"/></svg>PRICE
    </div>
    <div class="package-price"><span class="currency">$</span>195.00</div>
  </div>

  <div class="package package-week-3">
    <div class="package-title">3 WEEK<br>PACKAGE</div>
    <div class="package-days">(21 DAYS)</div>
    <div class="package-meals">2 MEALS PER DAY</div>
    <div class="package-price-label">
      <svg class="leaf" viewBox="0 0 26 22"><path d="M2 21 C2 9 10 2 25 1 C23 14 15 20 5 20 Z" fill="currentColor"/></svg>PRICE
    </div>
    <div class="package-price"><span class="currency">$</span>546.00</div>
  </div>

  <div class="save-badge badge-42">
    <span class="save-word">SAVE</span>
    <span class="save-amount"><span class="currency">$</span>42</span>
  </div>

  <div class="package package-week-6">
    <div class="package-title">6 WEEK<br>PACKAGE</div>
    <div class="package-days">(45 DAYS)</div>
  </div>

  <div class="save-badge badge-180">
    <span class="save-word">SAVE</span>
    <span class="save-amount"><span class="currency">$</span>180</span>
  </div>

  <div class="package-week-6-detail">
    <div class="package-meals">2 MEALS PER DAY</div>
    <div class="package-price-label">
      <svg class="leaf" viewBox="0 0 26 22"><path d="M2 21 C2 9 10 2 25 1 C23 14 15 20 5 20 Z" fill="currentColor"/></svg>PRICE
    </div>
    <div class="package-price"><span class="currency">$</span>1080.00</div>
  </div>

  <div class="app-strip">
    <div class="app-strip-label">Order Food easily on our APP</div>
    <div class="store-badge store-badge-a" role="img" aria-label="App store download badge"></div>
    <div class="store-badge store-badge-b" role="img" aria-label="Play store download badge"></div>
  </div>
  <p class="app-note">You can also download our mobile app from the play store and app store to choose your favorite meal from your favorite kitchen.</p>

  <div class="footer-strip">
    <svg width="900" height="18" viewBox="0 0 900 18" aria-hidden="true"><path d="M675 18 L700 0 H900 V18 Z" fill="var(--green)"/></svg>
  </div>
</div>
</body>
</html>
```